The Pipe Lantern business cards

Hi
i have attached a photo, this is how i want the front of my business card to look like:
i want the water drop on the right to be orange
and the water drop on the left to be gloss black
"The" and "Pty Ltd." will be in the same orange as the water drop
and "Pipe Lantern" will be in white
The background of the logo will be a matte black
on the back of the business card i need the following info:
'The Pipe Lantern pty ltd. '
'Plumbing . Drainage . Gas Fitting . Roofing . Jet Blasting . CCTV . '
Also my contact details:
Cal Yardley
0418672913
thepipelantern@mailkestrel.com
Licence# 583016K
Target Market(s)
Strata managers, building managers, the general public
Industry/Entity Type
Business

```html
<!DOCTYPE html>
<html lang="en">
<head>
<meta charset="utf-8">
<title>The Pipe Lantern – Business Card</title>
<link rel="stylesheet" href="https://fonts.googleapis.com/css2?family=Advent+Pro:wght@400;600&display=swap">
<style>
  :root {
    --paper: #ffffff;
    --ink: #111111;
    --brand-orange: #f28a1a;
    --brand-matte: #1c1c1c;
    --brand-white: #ffffff;
    --tap-blue: #1a8fce;
    --sea-pale: #d3e5f7;
    --sea-light: #5aa6e6;
    --sea-mid: #1f6cc4;
    --sea-deep: #0a2a66;
    --sea-night: #030c24;
  }
  * { margin: 0; padding: 0; box-sizing: border-box; }
  html, body {
    width: 720px;
    height: 1200px;
    overflow: hidden;
    background: var(--paper);
  }
  .card {
    position: relative;
    width: 720px;
    height: 1200px;
    background: var(--paper);
    font-family: "Advent Pro", "Arial Narrow", sans-serif;
    color: var(--ink);
    overflow: hidden;
  }
  .tap-icon {
    position: absolute;
    left: 299px;
    top: 59px;
    width: 133px;
    height: 117px;
    border-radius: 14px;
    background: linear-gradient(160deg, #2ea6e6, var(--tap-blue));
  }
  .services {
    position: absolute;
    top: 198px;
    left: 0;
    width: 100%;
    text-align: center;
    font-size: 30px;
    font-weight: 400;
    line-height: 38px;
    letter-spacing: 0.5px;
  }
  .brand {
    position: absolute;
    top: 306px;
    left: 30px;
    width: 660px;
    height: 200px;
    padding: 0 36px;
    display: flex;
    align-items: center;
    gap: 34px;
    background: var(--brand-matte);
    border-radius: 16px;
  }
  .brand-dot {
    flex: none;
    width: 130px;
    height: 130px;
    border-radius: 50%;
    background: var(--brand-orange);
  }
  .brand-name {
    font-size: 68px;
    font-weight: 600;
    line-height: 0.95;
    color: var(--brand-white);
  }
  .brand-name .suffix {
    display: block;
    font-size: 34px;
    line-height: 1.3;
  }
  .contact {
    position: absolute;
    z-index: 2;
    top: 540px;
    left: 0;
    width: 100%;
    text-align: center;
    font-style: normal;
    font-size: 39px;
    font-weight: 400;
    line-height: 57px;
    letter-spacing: 0.5px;
  }
  .contact .email { font-size: 37px; }
  .ripple-photo {
    position: absolute;
    z-index: 1;
    left: 0;
    top: 700px;
    width: 720px;
    height: 500px;
    background:
      radial-gradient(ellipse 260px 110px at 352px 270px, var(--sea-night) 0%, var(--sea-deep) 45%, transparent 100%),
      linear-gradient(180deg, var(--paper) 0%, var(--paper) 10%, var(--sea-pale) 16%, var(--sea-light) 26%, var(--sea-mid) 46%, var(--sea-deep) 74%, var(--sea-night) 100%);
  }
</style>
</head>
<body>
  <main class="card">
    <div class="tap-icon" role="img" aria-label="Blue water tap icon"></div>

    <p class="services">Plumbing . Drainage . Gas Fitting . Roofing .<br>Jet Blasting . CCTV .</p>

    <div class="brand">
      <span class="brand-dot" aria-hidden="true"></span>
      <h1 class="brand-name">The Pipe<br>Lantern<span class="suffix">pty ltd.</span></h1>
    </div>

    <address class="contact">
      <div class="name">Cal Yardley</div>
      <div class="phone">0418672913</div>
      <div class="email">thepipelantern@mailkestrel.com</div>
      <div class="licence">Licence # 583016K</div>
    </address>

    <div class="ripple-photo" role="img" aria-label="Photograph of a water droplet falling into blue water with spreading ripples"></div>
  </main>
</body>
</html>
```